Quote Cards With TK May 2025 for Instagram

I would like to put these quotes over one of the pictures attached; Instagram (new size: 4:5 (1080 x 1350 pixels) One Quote per picture, and I want the quote to be bold or easy to read as well. I provided a few reference graphics that I really like as examples below. In very small letters at the bottom add @TKBarlowOnline

All of the pictures are attached; you can pick any photo and add one quote to it; but no stock photography

```html
<!DOCTYPE html>
<html lang="en">
<head>
<meta charset="utf-8">
<title>Quote Cards With TK — May 2025</title>
<link rel="stylesheet" href="https://fonts.googleapis.com/css2?family=Anton&family=Oswald:wght@500;700&display=swap">
<style>
:root{
  --page:#ffffff;
  --white:#ffffff;
  --yellow:#ffd21f;
  --pink:#ff3fa4;
  --purple-deep:#3b0f63;
  --purple:#7b2cbf;
  --violet:#8a2be2;
  --blue:#1e5bb8;
  --orange:#e2731c;
  --black:#0c0c0c;
  --magenta:#c0127a;
  --navy:#241a5c;
  --skin:#7a4a35;
}
*{margin:0;padding:0;box-sizing:border-box}
html,body{width:1200px;height:4000px;overflow:hidden;background:var(--page)}
.sheet{position:relative;width:1200px;height:4000px}
.card{position:absolute;width:480px;height:600px;overflow:hidden;color:var(--white);
  font-family:'Anton',sans-serif;text-transform:uppercase;line-height:1.02}
.col-a{left:80px}.col-b{left:628px}
.row-1{top:112px}.row-2{top:816px}.row-3{top:1520px}.row-4{top:2224px}.row-5{top:2928px}
.photo{position:absolute}
.quote{position:absolute}
.handle{position:absolute;bottom:22px;font-family:'Oswald',sans-serif;font-weight:700;
  font-size:17px;text-transform:none;display:flex;align-items:center;gap:6px;color:var(--white)}
.handle::before{content:"";width:12px;height:12px;border-radius:50%;background:var(--yellow)}
.handle.boxed{border:2px solid var(--white);padding:4px 8px;font-size:13px;text-transform:uppercase}
.handle.boxed::before{display:none}
.y{color:var(--yellow)}.p{color:var(--pink)}
.small{font-family:'Oswald',sans-serif;font-weight:700}

/* 1 */
.c1{background:linear-gradient(160deg,#8b2fc9,#4a1180)}
.c1 .photo{left:110px;top:40px;width:260px;height:560px;border-radius:130px 130px 0 0;
  background:linear-gradient(180deg,#2a1a2e,#141014)}
.c1 .quote{right:26px;top:320px;width:230px;text-align:center;font-size:30px}
.c1 .fix{font-size:68px;color:var(--yellow)}
.c1 .handle{left:22px}

/* 2 */
.c2{background:linear-gradient(135deg,#f08a2c,#6b2a10 60%,#1b0d06)}
.c2 .photo{left:0;top:50px;width:210px;height:550px;background:linear-gradient(180deg,#3a2418,#0e0a08)}
.c2 .quote{right:22px;top:30px;width:270px;text-align:right;font-size:37px}
.c2 .big{font-size:70px;margin-top:14px}
.c2 .handle{left:22px}

/* 3 */
.c3{background:linear-gradient(180deg,#2f7fd8,#143f8e)}
.c3 .photo{left:0;top:150px;width:220px;height:450px;background:linear-gradient(180deg,#4a3025,#1a1210)}
.c3 .head{position:absolute;top:26px;left:0;right:0;text-align:center;font-size:74px}
.c3 .quote{right:24px;top:132px;width:250px;text-align:center;font-size:34px}
.c3 .quote .cta{font-size:26px;margin-top:12px}
.c3 .quote .bye{font-size:44px;color:var(--yellow)}
.c3 .handle{left:22px}

/* 4 */
.c4{background:linear-gradient(160deg,#9a35e0,#5b17a6)}
.c4 .photo{left:20px;top:210px;width:190px;height:390px;background:linear-gradient(180deg,#ff6fb8,#b02a78)}
.c4 .quote{left:24px;top:28px;right:24px;font-size:44px;text-align:right}
.c4 .quote .first{text-align:left}
.c4 .quote .next{font-size:80px;text-align:center;margin-top:18px}
.c4 .handle{right:24px}

/* 5 */
.c5{background:var(--black)}
.c5 .photo{left:100px;top:20px;width:280px;height:340px;background:radial-gradient(ellipse at 50% 40%,#3a3a3a,#0c0c0c 70%)}
.c5 .quote{left:30px;right:30px;top:370px;text-align:center;font-size:32px}
.c5 .handle{left:0;right:0;justify-content:center}

/* 6 */
.c6{background:linear-gradient(180deg,#5c6470,#2b2f38)}
.c6 .photo{inset:0;background:linear-gradient(180deg,#8c93a0 0%,#4a4f5a 55%,#20232a)}
.c6 .shade{position:absolute;left:0;right:0;bottom:0;height:330px;background:linear-gradient(180deg,transparent,rgba(0,0,0,.75))}
.c6 .quote{right:26px;top:300px;width:270px;text-align:center;font-size:29px}
.c6 .quote .cmt{font-family:'Oswald',sans-serif;text-transform:none;font-size:20px;margin-top:8px}
.c6 .quote .skinny{font-size:42px;color:var(--pink)}
.c6 .quote .tail{font-size:20px}
.c6 .handle{right:26px}

/* 7 */
.c7{background:linear-gradient(150deg,#e0208e,#6e0a5c)}
.c7 .photo{right:0;top:40px;width:210px;height:560px;background:linear-gradient(180deg,#c23aa0,#4a0f3e)}
.c7 .quote{left:26px;top:30px;width:260px;font-size:40px}
.c7 .quote .right{font-size:56px;color:var(--yellow)}
.c7 .quote .answer{font-size:54px;color:var(--yellow);margin-top:16px}
.c7 .handle{left:26px}

/* 8 */
.c8{background:linear-gradient(160deg,#7a2ad0,#3d1080)}
.c8 .photo{right:0;top:150px;width:220px;height:450px;background:linear-gradient(180deg,#f2e8f0,#2a1a30)}
.c8 .quote{left:26px;top:26px;right:26px;font-size:50px}
.c8 .quote .body{width:230px;font-size:30px;margin-top:14px;border-left:4px solid var(--yellow);padding-left:12px}
.c8 .quote .cta{width:230px;font-size:20px;margin-top:14px;font-family:'Oswald',sans-serif}
.c8 .handle{left:26px}

/* 9 */
.c9{background:linear-gradient(160deg,#d8186e,#7a0d4a)}
.c9 .photo{right:0;top:110px;width:220px;height:490px;background:linear-gradient(180deg,#3a2330,#120a10)}
.c9 .quote{left:26px;top:30px;width:250px;font-size:62px}
.c9 .quote .sub{font-family:'Oswald',sans-serif;font-size:24px;margin-top:14px;color:var(--yellow)}
.c9 .quote .fix{font-size:40px;margin-top:14px;color:var(--yellow)}
.c9 .handle{left:26px}

/* 10 */
.c10{background:linear-gradient(160deg,#3a2a8c,#1a1140)}
.c10 .photo{right:10px;top:60px;width:200px;height:540px;background:linear-gradient(180deg,#2c2430,#0e0a12)}
.c10 .quote{left:26px;top:30px;width:260px;font-size:58px}
.c10 .quote .fault{font-size:40px;color:var(--yellow);margin-top:12px}
.c10 .quote .body{font-family:'Oswald',sans-serif;font-size:22px;margin-top:16px}
.c10 .handle{left:26px}
</style>
</head>
<body>
<main class="sheet">

  <section class="card c1 col-a row-1">
    <div class="photo" role="img" aria-label="Photo of TK in black outfit pointing down"></div>
    <p class="quote">The stubborn belly fat after 40? It's not about calories it's about your hormones here is the <span class="fix">fix!</span></p>
    <p class="handle">@TKBarlowOnline</p>
  </section>

  <section class="card c2 col-b row-1">
    <div class="photo" role="img" aria-label="Photo of TK standing in black outfit"></div>
    <p class="quote"><span class="y">Bloating. Muffin top. Puffy waistline.</span><br>Your body's screaming for a different kind of fix.<span class="big" style="display:block">Here it is</span></p>
    <p class="handle">@TKBarlowOnline</p>
  </section>

  <section class="card c3 col-a row-2">
    <p class="head">Flat tummy</p>
    <div class="photo" role="img" aria-label="Photo of TK smiling in black top"></div>
    <div class="quote">
      <p class="y" style="font-size:44px">In your 40s?</p>
      <p>It's still possible!</p>
      <p class="cta">Comment</p>
      <p class="bye">Bye belly</p>
      <p class="cta" style="margin-top:4px">to get the 10 secrets to a flatter tummy</p>
    </div>
    <p class="handle">@TKBarlowOnline</p>
  </section>

  <section class="card c4 col-b row-2">
    <div class="photo" role="img" aria-label="Photo of TK in pink outfit"></div>
    <div class="quote">
      <p class="first">This 90-day plan</p>
      <p>helped women<br>over 40<br>slim down,<br>get a tiny<br>waist and feel<br>sexy again.</p>
      <p class="next">You're next.</p>
    </div>
    <p class="handle">@TKBarlowOnline</p>
  </section>

  <section class="card c5 col-a row-3">
    <div class="photo" role="img" aria-label="Photo of TK from behind in black outfit"></div>
    <p class="quote"><span class="p">What worked in your 30s won't work now.</span><br>Here's what actually does.<br><span class="p">Drop 30 pounds in 3 months.</span></p>
    <p class="handle">@TKBarlowOnline</p>
  </section>

  <section class="card c6 col-b row-3">
    <div class="photo" role="img" aria-label="Photo of TK cheering in a crowd at a courtside game"></div>
    <div class="shade"></div>
    <div class="quote">
      <p>This is the secret women over 40 are using to get snatched; without starving</p>
      <p class="cmt">Comment</p>
      <p class="skinny">Skinny</p>
      <p class="tail">to get the exact plan.</p>
    </div>
    <p class="handle">@TKBarlowOnline</p>
  </section>

  <section class="card c7 col-a row-4">
    <div class="photo" role="img" aria-label="Photo of TK in pink dress"></div>
    <div class="quote">
      <p>You're doing all the</p>
      <p class="right">“Right”</p>
      <p>things, but your belly won't go down?</p>
      <p class="answer">Here's what you haven't</p>
    </div>
    <p class="handle">@TKBarlowOnline</p>
  </section>

  <section class="card c8 col-b row-4">
    <div class="photo" role="img" aria-label="Photo of TK in white top and black pants"></div>
    <div class="quote">
      <p>Your belly<br>isn't fat...<br>it's hormonal</p>
      <p class="body y">And here's how to fix it</p>
      <p class="cta">Comment hormones if nothing is working.</p>
    </div>
    <p class="handle boxed">@TKBarlowOnline</p>
  </section>

  <section class="card c9 col-a row-5">
    <div class="photo" role="img" aria-label="Photo of TK in black outfit"></div>
    <div class="quote">
      <p>Tired.<br>Moody.<br>Stubborn<br>belly fat.</p>
      <p class="sub">Your hormones are screaming for help!</p>
      <p class="fix">Let's fix that</p>
    </div>
    <p class="handle boxed">@TKBarlowOnline</p>
  </section>

  <section class="card c10 col-b row-5">
    <div class="photo" role="img" aria-label="Photo of TK in sheer black outfit"></div>
    <div class="quote">
      <p>That stubborn weight?</p>
      <p class="fault">It's not your fault.</p>
      <p class="body">Your hormones are to blame and you're not alone; but there is a fix.</p>
    </div>
    <p class="handle boxed">@TKBarlowOnline</p>
  </section>

</main>
</body>
</html>
```